TAVRO Capital Group LLC a High Risk Big Rewards company for Rich Young Entrepreneurs

We would like a very modern, powerful in the eyes of our customers, modern, minimalist feel, financial gain. this business card is for young Rich entrepreneurs who want to invest money into High Risk, Big Rewards Businesses. The card Should sell the business!! let your creativity go Wild! I pick most of the designers for this project because of your BOLD Designs, I would like this card to be Bold, Modern, Minimalist, use as many effects in your graphic Artist Mind, Do not let the Financial sound of this business to make you think Conservative that's the last thing we are! if you have a lot of money and you want to play a risky market call US
Updates

Project Deadline Extended
Reason: have not received, enough designs to choose 1st and second place, sure I have received over 100 designs but it seems most designers are submitting every card they have ever made before and calling it mine, please we are looking for fresh ideas please!

Target Market(s)

Private Risky Investors

Industry/Entity Type

Financial

Contact Information for Business Card

powerful in the eyes of our customers,modern, minimalist feel

Font styles to use
Other font styles liked:
• Modern feeling fonts

Requirements
Must have
• The Company Name is TAVRO Capital Group LLC and it must be on the CARD
• My Name, title, Cell , email
• Delvin Ashcroft G.E.D.
• Managing Member
• 555.038.6195
• delvin@tavrocapitalgroup.example
Nice to have
• try a black thick plastic card with round corners with Delvin Ashcroft GED (make sure GED is smaller than name) just on one side of the card, and my phone number with out the icons and email on the other side, this card should look like a exclusive credit card or exclusive VIP card, something you would never loose

```html
<!DOCTYPE html>
<html lang="en">
<head>
<meta charset="utf-8">
<title>Delvin Ashcroft — TAVRO Capital Group LLC</title>
<link href="https://fonts.googleapis.com/css2?family=Lato:wght@300;400&family=Oswald:wght@300;400&display=swap" rel="stylesheet">
<style>
  :root {
    --backdrop: #161616;
    --card: #2a2a2a;
    --card-edge: #353535;
    --ink: #a3a3a3;
    --ink-soft: #767676;
    --metal: #8c8c8c;
  }
  * { box-sizing: border-box; margin: 0; padding: 0; }
  html, body {
    width: 1200px;
    height: 780px;
    overflow: hidden;
    background: var(--backdrop);
  }
  .stage {
    width: 1200px;
    height: 780px;
    display: flex;
    align-items: center;
    justify-content: center;
    gap: 60px;
  }
  .card {
    position: relative;
    width: 520px;
    height: 330px;
    background: var(--card);
    border: 1px solid var(--card-edge);
    border-radius: 22px;
  }
  .metal-tab {
    position: absolute;
    background: var(--metal);
    border-radius: 1px;
  }
  .metal-tab--top { top: -2px; left: 70px; width: 22px; height: 5px; }
  .metal-tab--side { right: -2px; bottom: 48px; width: 5px; height: 22px; }

  .identity {
    position: absolute;
    top: 118px;
    left: 0;
    right: 0;
    text-align: center;
    font-family: "Lato", sans-serif;
  }
  .identity__name {
    font-weight: 400;
    font-size: 32px;
    line-height: 1.2;
    color: var(--ink);
    letter-spacing: 0.2px;
  }
  .identity__suffix {
    font-weight: 300;
    font-size: 21px;
    color: var(--ink-soft);
    margin-left: 6px;
  }
  .identity__title {
    margin-top: 8px;
    font-weight: 300;
    font-size: 11px;
    letter-spacing: 4px;
    text-transform: uppercase;
    color: var(--ink-soft);
  }

  .company {
    position: absolute;
    top: 34px;
    right: 34px;
    font-family: "Lato", sans-serif;
    font-weight: 400;
    font-size: 11px;
    letter-spacing: 3px;
    text-transform: uppercase;
    color: var(--ink-soft);
  }
  .contact {
    position: absolute;
    left: 34px;
    bottom: 42px;
  }
  .contact__phone {
    font-family: "Oswald", sans-serif;
    font-weight: 400;
    font-size: 18px;
    letter-spacing: 1px;
    line-height: 1.3;
    color: var(--ink);
  }
  .contact__email {
    margin-top: 4px;
    font-family: "Lato", sans-serif;
    font-weight: 400;
    font-size: 15px;
    color: var(--ink);
  }
</style>
</head>
<body>
  <main class="stage">
    <section class="card card--front" aria-label="Card front">
      <span class="metal-tab metal-tab--top"></span>
      <span class="metal-tab metal-tab--side"></span>
      <div class="identity">
        <h1 class="identity__name">Delvin Ashcroft<span class="identity__suffix">GED</span></h1>
        <p class="identity__title">Managing Member</p>
      </div>
    </section>

    <section class="card card--back" aria-label="Card back">
      <p class="company">TAVRO Capital Group LLC</p>
      <div class="contact">
        <p class="contact__phone">555.038.6195</p>
        <p class="contact__email">delvin@tavrocapitalgroup.example</p>
      </div>
    </section>
  </main>
</body>
</html>
```